web site to find a reliable, local tradesman, handyman or builder for any job

Design a web site as marketplace for handyman and client.
Handyman can
* set their profile (name, address, contacts)
* search / view / apply for job offers (by setting a new offer)
Client can
* search / view job offers
* generate new job offers (title, description, max price, date, duration, location).
* select and rate a job
Main functions would be SEARCH / VIEW to see in one glance WHAT needs to be done WHERE. The contractors then exchange contacts.
Handyman

```html
<!DOCTYPE html>
<html lang="en">
<head>
<meta charset="utf-8">
<title>Handfinder – find a local tradesman</title>
<link href="https://fonts.googleapis.com/css2?family=PT+Sans:wght@400;700&family=Arimo:wght@400&display=swap" rel="stylesheet">
<style>
:root{
  --ink:#141414;
  --header-top:#262626;
  --header-bottom:#101010;
  --nav-top:#2c2c2c;
  --nav-bottom:#151515;
  --hero-bg:#1d1d1d;
  --field:#2b2b29;
  --field-text:#b9b9b2;
  --olive-light:#b3b63c;
  --olive-dark:#878a1c;
  --olive-active:#9a9d25;
  --lime-top:#e2e65a;
  --lime-bottom:#a7ab1d;
  --white:#ffffff;
  --body-text:#5a5a5a;
  --heading:#2a2a2a;
  --red:#e01010;
  --band-top:#ececec;
  --band-bottom:#c9c9c9;
  --badge:#4a4a4a;
  --social:#6f6f6f;
}
*{box-sizing:border-box;margin:0;padding:0}
html,body{width:1032px;height:1200px;overflow:hidden;background:var(--white)}
body{position:relative;font-family:"PT Sans",sans-serif;color:var(--ink)}
.abs{position:absolute}

/* header */
.site-header{position:absolute;left:0;top:0;width:1032px;height:132px;background:linear-gradient(var(--header-top),var(--header-bottom))}
.brand{position:absolute;left:26px;top:38px;display:flex;align-items:center;gap:12px}
.brand-dot{width:44px;height:44px;border-radius:50%;background:#e8417b}
.brand-name{font-size:38px;font-weight:700;color:#e6e6e6;letter-spacing:-.5px}
.user-login{position:absolute;left:744px;top:12px;width:240px}
.user-login h2{font-size:12px;font-weight:400;color:var(--white);margin-left:12px}
.pill{position:absolute;height:27px;border-radius:14px;background:var(--field);box-shadow:inset 0 2px 3px #000,0 1px 0 #3b3b3b;color:var(--field-text);font-family:"PT Sans",sans-serif;font-size:12.5px;line-height:27px;padding-left:14px}
.round-btn{position:absolute;width:40px;height:40px;border-radius:50%;background:linear-gradient(var(--lime-top),var(--lime-bottom));border:2px solid #3a3a12;font-size:11.5px;line-height:36px;text-align:center;color:#1a1a1a}
.forgot{position:absolute;font-size:11px;color:#5b5b55}

/* nav */
.main-nav{position:absolute;left:0;top:132px;width:1032px;height:61px;background:linear-gradient(var(--nav-top),var(--nav-bottom));border-top:1px solid #3c3c3c;border-bottom:1px solid #080808}
.main-nav a{position:absolute;top:0;height:60px;line-height:60px;font-size:20px;color:#f2f2f2;text-decoration:none;text-align:center}
.main-nav a.is-active{background:var(--olive-active);color:#fff;border:1px solid #b9bc45}

/* hero */
.hero{position:absolute;left:0;top:193px;width:1032px;height:330px;background:var(--hero-bg)}
.hero-photo{position:absolute;left:66px;top:1px;width:616px;height:320px;background:linear-gradient(100deg,#6b3a2c 0%,#7d4332 40%,#5d3a28 70%,#3c2a1e 100%)}
.hero-caption{position:absolute;left:0;bottom:0;width:100%;height:46px;background:rgba(0,0,0,.55);color:#d8d8d8;font-family:"Arimo",sans-serif;font-size:12.5px;line-height:46px;padding-left:23px}
.slide-arrow{position:absolute;top:141px;width:30px;height:30px;border-radius:50%;background:rgba(120,120,120,.7);border:2px solid rgba(210,210,210,.7)}
.hero-search{position:absolute;left:718px;top:34px;width:260px}
.hero-search h2{font-size:25px;font-weight:400;color:#e4e4e4;margin-left:8px}
.search-field{position:absolute;left:2px;top:40px;width:253px;height:37px;border-radius:18px;background:#2e2e2e;box-shadow:inset 0 2px 3px #000}
.choice{position:absolute;left:80px;font-family:"Arimo",sans-serif;font-size:12.5px;color:#e8e8e8;display:flex;align-items:center;gap:12px}
.choice i{width:11px;height:11px;border-radius:50%;background:#6a6a6a;display:block}
.choice i.on{background:#c42a2a;box-shadow:0 0 0 2px #6a6a6a}
.lime-btn{position:absolute;height:33px;border-radius:17px;background:linear-gradient(var(--lime-top),var(--lime-bottom));border:1px solid #50520f;text-align:center;font-size:15px;line-height:31px;color:#1a1a1a}

/* forms band */
.forms-band{position:absolute;left:0;top:523px;width:1032px;height:207px;background:linear-gradient(var(--olive-light),var(--olive-dark))}
.band-title{position:absolute;top:24px;font-size:25px;font-weight:700;color:#2c2c2c;text-shadow:0 1px 0 rgba(255,255,255,.3)}
.divider{position:absolute;left:271px;top:22px;width:3px;height:166px;background:#7a7d19;border-right:1px solid #c2c55a}
.dark-forgot{position:absolute;left:36px;top:152px;font-size:12px;color:#2a2a18}
.select-tab{position:absolute;right:0;top:0;width:31px;height:27px;border-radius:0 14px 14px 0;background:#8f921e;border-left:1px solid #5c5e10}

/* about */
.section-title{position:absolute;left:28px;font-size:25px;font-weight:400;color:var(--heading);text-shadow:0 1px 1px #aaa}
.about-photo{position:absolute;left:30px;top:792px;width:179px;height:127px;border:3px solid #fff;box-shadow:1px 1px 3px #999;background:linear-gradient(160deg,#5f8cc8 0%,#a9c2de 35%,#b9874f 60%,#7e5a34 100%)}
.about-text{position:absolute;left:225px;top:791px;width:764px;font-family:"Arimo",sans-serif;font-size:12.4px;line-height:18.5px;color:var(--body-text)}
.read-more{position:absolute;left:930px;top:903px;font-family:"Arimo",sans-serif;font-size:12.4px;color:var(--red);text-decoration:none}

/* partners */
.partners{position:absolute;left:0;top:996px;width:1032px;height:100px;background:linear-gradient(var(--band-top),var(--band-bottom));border-bottom:3px solid #e6e6e6}
.badge{position:absolute;background:var(--badge)}

/* footer */
.site-footer{position:absolute;left:0;top:1099px;width:1032px;height:101px;background:#000;color:#fff}
.footer-links{position:absolute;left:0;width:1032px;top:22px;text-align:center;font-size:12px}
.footer-links a{color:#fff;text-decoration:none}
.copyright{position:absolute;left:0;width:1032px;top:53px;text-align:center;font-size:12px}
.connect{position:absolute;left:911px;top:20px;font-size:12px}
.social{position:absolute;top:42px;width:33px;height:33px;border-radius:5px;background:var(--social)}
</style>
</head>
<body>

<header class="site-header">
  <div class="brand"><span class="brand-dot"></span><span class="brand-name">Handfinder</span></div>
  <div class="user-login">
    <h2>User Log in</h2>
  </div>
  <div class="pill" style="left:745px;top:33px;width:222px">User Name</div>
  <div class="pill" style="left:745px;top:72px;width:222px">Password</div>
  <div class="round-btn" style="left:942px;top:46px">Log in</div>
  <div class="forgot" style="left:757px;top:107px">Forget Pasword?</div>
</header>

<nav class="main-nav">
  <a class="is-active" href="#" style="left:53px;width:96px">About</a>
  <a href="#" style="left:170px;width:94px">Services</a>
  <a href="#" style="left:310px;width:90px">News</a>
  <a href="#" style="left:445px;width:92px">Projects</a>
  <a href="#" style="left:592px;width:94px">Partners</a>
  <a href="#" style="left:745px;width:94px">Supports</a>
  <a href="#" style="left:900px;width:90px">Contact</a>
</nav>

<section class="hero">
  <div class="hero-photo" role="img" aria-label="Photo of a smiling handyman with a tool belt in front of a brick house, a worker on a ladder behind him">
    <div class="slide-arrow" style="left:11px"></div>
    <div class="slide-arrow" style="right:11px"></div>
    <div class="hero-caption">Et harum quidem rerum facilis est et expedita distinctio.</div>
  </div>
  <div class="hero-search">
    <h2>Search</h2>
    <div class="search-field"></div>
    <div class="choice" style="top:125px"><i class="on"></i>Handyman</div>
    <div class="choice" style="top:158px"><i></i>Constructor</div>
    <div class="choice" style="top:191px"><i></i>Builders</div>
    <div class="lime-btn" style="left:68px;top:231px;width:121px">Search</div>
  </div>
</section>

<section class="forms-band">
  <h2 class="band-title" style="left:29px">Member Login</h2>
  <div class="pill" style="left:22px;top:71px;width:223px">Member Name</div>
  <div class="pill" style="left:22px;top:110px;width:223px">Password</div>
  <div class="round-btn" style="left:220px;top:84px">Log in</div>
  <div class="dark-forgot">Forget Pasword?</div>
  <div class="divider"></div>

  <h2 class="band-title" style="left:296px">Job Offers</h2>
  <div class="pill" style="left:290px;top:71px;width:223px">Title</div>
  <div class="pill" style="left:290px;top:110px;width:223px">Description</div>
  <div class="pill" style="left:538px;top:71px;width:223px">Max price</div>
  <div class="pill" style="left:538px;top:110px;width:109px">Date</div>
  <div class="pill" style="left:651px;top:110px;width:110px">Duration</div>
  <div class="pill" style="left:787px;top:71px;width:224px">Location<span class="select-tab"></span></div>
  <div class="lime-btn" style="left:839px;top:109px;width:110px">Generate</div>
</section>

<h2 class="section-title" style="top:746px">About Us</h2>
<div class="about-photo" role="img" aria-label="Photo of two builders in hard hats reading plans under a timber frame"></div>
<p class="about-text">At vero eos et accusamus et iusto odio dignissimos ducimus qui blanditiis praesentium voluptatum deleniti atque corrupti quos dolores et quas molestias excepturi sint occaecati cupiditate non provident, similique sunt in culpa qui officia deserunt mollitia animi, id est laborum et dolorum fuga. Et harum quidem rerum facilis est et expedita distinctio.Nor again is there anyone who loves or pursues or desires to obtain pain of itself, because it is pain, but because occasionally circumstances occur in which toil and pain can procure him some great pleasure. Itaque earum rerum hic tenetur a sapiente delectus, ut aut reiciendis voluptatibus maiores alias consequatur aut perferendis doloribus asperiores repellat.</p>
<a class="read-more" href="#">read more</a>

<h2 class="section-title" style="top:963px">Our Partners</h2>
<section class="partners" aria-label="Partner badges">
  <div class="badge" style="left:34px;top:20px;width:84px;height:56px;border-radius:4px"></div>
  <div class="badge" style="left:185px;top:14px;width:62px;height:62px"></div>
  <div class="badge" style="left:315px;top:9px;width:87px;height:72px;border-radius:6px"></div>
  <div class="badge" style="left:468px;top:10px;width:66px;height:68px;border-radius:50%"></div>
  <div class="badge" style="left:592px;top:28px;width:105px;height:30px"></div>
  <div class="badge" style="left:734px;top:24px;width:104px;height:38px;border-radius:4px"></div>
  <div class="badge" style="left:857px;top:26px;width:145px;height:34px"></div>
</section>

<footer class="site-footer">
  <nav class="footer-links">
    <a href="#">About</a> | <a href="#">Services</a> | <a href="#">News</a> | <a href="#">Projects</a> | <a href="#">Partners</a> | <a href="#">Supports</a> | <a href="#">Contact</a>
  </nav>
  <p class="copyright">© All Copyrights.Handfinder.Reserved</p>
  <p class="connect">Connect with us:</p>
  <span class="social" style="left:888px" role="img" aria-label="Social network link"></span>
  <span class="social" style="left:929px" role="img" aria-label="Social network link"></span>
  <span class="social" style="left:970px" role="img" aria-label="News feed link"></span>
</footer>

</body>
</html>
```